Professional business card design for Shelfwright Company
Biz card design utilizing existing Logo
Professional business card design for Shelfwright Company - Construction
Creative Brief
Use same font as used in my logo
Dean Halvik
President
not necessary
dean@brvmarrow.com
www.brvmarrow.com

```html
<!DOCTYPE html>
<html lang="en">
<head>
<meta charset="utf-8">
<title>Shelfwright Company – Business Card</title>
<link rel="stylesheet" href="https://fonts.googleapis.com/css2?family=Oswald:wght@400;700&family=Open+Sans:ital,wght@0,400;0,600;1,400&display=swap">
<style>
  :root{
    --bg:#e9e9ea;
    --card:#ffffff;
    --card-shade:#e4e5e6;
    --ink:#1d1d1f;
    --grey:#5d5f63;
    --title-blue:#4a4fa8;
    --green-dark:#1f5a12;
    --green:#3f8f1c;
    --green-light:#7dc242;
    --band-dark:#151515;
  }
  *{box-sizing:border-box;margin:0;padding:0}
  html,body{width:1200px;height:869px;overflow:hidden;background:var(--bg)}
  .canvas{width:1200px;height:869px;display:flex;flex-direction:column;align-items:center;justify-content:center;gap:40px}
  .card{position:relative;width:660px;height:377px;overflow:hidden;box-shadow:0 10px 26px rgba(0,0,0,.18)}
  .card--back{background:var(--card);display:flex;align-items:center;justify-content:center}
  .card--front{background:radial-gradient(ellipse at 55% 40%,var(--card) 0%,var(--card) 45%,var(--card-shade) 100%)}
  .brand{display:flex;align-items:center;gap:12px}
  .brand__square{width:58px;height:58px;background:linear-gradient(135deg,var(--green-light),var(--green-dark))}
  .brand__name{font-family:"Oswald",sans-serif;font-weight:700;text-transform:uppercase;color:var(--ink);line-height:1;letter-spacing:.5px}
  .card--back .brand__name{font-size:40px}
  .card--front .brand{position:absolute;left:40px;top:34px}
  .card--front .brand__square{width:48px;height:48px}
  .card--front .brand__name{font-size:32px}
  .contacts{position:absolute;left:42px;top:118px;list-style:none;font-family:"Open Sans",sans-serif;font-size:12px;color:var(--grey)}
  .contacts li{display:flex;align-items:center;gap:9px;height:22px}
  .contacts svg{width:12px;height:12px;fill:var(--ink)}
  .person{position:absolute;right:46px;top:158px;text-align:right;font-family:"Open Sans",sans-serif}
  .person__name{font-family:"Oswald",sans-serif;font-weight:400;font-size:24px;letter-spacing:1.5px;text-transform:uppercase;color:var(--grey)}
  .person__title{font-style:italic;font-size:13px;color:var(--title-blue);margin-top:2px}
  .person__address{font-size:13px;color:var(--grey);margin-top:16px;line-height:1.45}
  .swoosh{position:absolute;left:0;bottom:0;width:660px;height:377px}
  .website{position:absolute;right:120px;bottom:22px;font-family:"Open Sans",sans-serif;font-weight:600;font-size:14px;letter-spacing:3px;color:#fff}
</style>
</head>
<body>
<main class="canvas">
  <section class="card card--back" aria-label="Card back">
    <div class="brand">
      <span class="brand__square"></span>
      <span class="brand__name">Shelfwright Company</span>
    </div>
  </section>

  <section class="card card--front" aria-label="Card front">
    <svg class="swoosh" viewBox="0 0 660 377" aria-hidden="true">
      <defs>
        <linearGradient id="bandGreen" x1="0" y1="0" x2="1" y2="0">
          <stop offset="0" stop-color="#1f5a12"/>
          <stop offset=".45" stop-color="#3f8f1c"/>
          <stop offset="1" stop-color="#2d7014"/>
        </linearGradient>
      </defs>
      <path d="M0 255 C160 262 360 300 660 318 L660 377 L0 377 Z" fill="var(--band-dark)"/>
      <path d="M0 266 C170 276 370 312 660 326 L660 377 L0 377 Z" fill="url(#bandGreen)"/>
      <path d="M0 266 C170 276 370 312 660 326" fill="none" stroke="#9ad65b" stroke-width="1.2" opacity=".7"/>
    </svg>

    <div class="brand">
      <span class="brand__square"></span>
      <span class="brand__name">Shelfwright Company</span>
    </div>

    <ul class="contacts">
      <li><svg viewBox="0 0 24 24"><path d="M6.6 10.8a15.1 15.1 0 0 0 6.6 6.6l2.2-2.2a1 1 0 0 1 1-.25 11.4 11.4 0 0 0 3.6.57 1 1 0 0 1 1 1V20a1 1 0 0 1-1 1A17 17 0 0 1 3 4a1 1 0 0 1 1-1h3.5a1 1 0 0 1 1 1c0 1.25.2 2.45.57 3.57a1 1 0 0 1-.25 1z"/></svg>555 014 2276</li>
      <li><svg viewBox="0 0 24 24"><rect x="6" y="1" width="12" height="22" rx="2"/></svg>555 014 2277</li>
      <li><svg viewBox="0 0 24 24"><rect x="2" y="9" width="20" height="11" rx="1"/><rect x="6" y="3" width="12" height="7"/></svg>555 014 2278</li>
      <li><svg viewBox="0 0 24 24"><path d="M2 5h20v14H2z M2 5l10 8 10-8" /></svg>dean@brvmarrow.com</li>
    </ul>

    <div class="person">
      <p class="person__name">Dean Halvik</p>
      <p class="person__title">President</p>
      <p class="person__address">41 Cedar Row, Suite 8<br>Halden Park Road</p>
    </div>

    <p class="website">www.brvmarrow.com</p>
  </section>
</main>
</body>
</html>
```